Ecommerce Website For Printing Company

Quillbrook.com are a print, design and signage company who sell flyers, business cards, posters, brochures and more to customers in the UK.

Our website is outdated and requires a new design using current web styling and mobile functionality.

We require the following pages to be designed;
- Home Page
- Price Page
- Portfolio Page
- Blog
- Content Page

Our competitors in the printing industry are www.venturaprint.com, www.lanternpress.co.uk, gableinkworks.co.uk, www.paperhaven.co.uk

We require the website to give a professional image as well as be easy for customers to navigate, understand and find prices.

Target Market(s)

Businesses

Industry/Entity Type

Printing

Number of Pages Required

4 page

Font styles to use
Sans Serif

Colors
33a6d7

Requirements
Must have
• Popular products, latest news/blog, sales from portfolio, newsletter sign up, footer

```html
<!DOCTYPE html>
<html lang="en">
<head>
<meta charset="utf-8">
<title>Quillbrook.com – Flyer, Leaflet and Brochure Printing</title>
<link rel="stylesheet" href="https://fonts.googleapis.com/css2?family=Open+Sans:wght@400;600;700&family=Raleway:wght@500;600;700;800&display=swap">
<style>
:root{
  --blue:#33a6d7;
  --blue-dark:#1f86b3;
  --red:#e2312d;
  --ink:#333;
  --muted:#777;
  --line:#e2e2e2;
  --band:#efefef;
  --footer:#2c2c2c;
  --footer-base:#1f1f1f;
  --white:#fff;
}
*{box-sizing:border-box;margin:0;padding:0}
html,body{width:1200px;height:2848px;overflow:hidden}
body{font-family:"Open Sans",Arial,sans-serif;color:var(--ink);background:var(--white);font-size:14px;line-height:1.5}
h1,h2,h3,h4{font-family:"Raleway","Open Sans",sans-serif}
.wrap{width:1120px;margin:0 auto;position:relative}

/* header */
.site-header{height:140px}
.site-header .wrap{display:flex;align-items:center;height:140px;justify-content:space-between}
.brand{display:flex;align-items:center;gap:14px}
.brand-square{width:36px;height:36px;background:var(--blue)}
.brand-name{font-family:"Raleway",sans-serif;font-weight:800;font-size:40px;color:var(--blue);letter-spacing:-.5px}
.header-right{display:flex;align-items:center;gap:22px}
.live-chat{display:flex;align-items:center;gap:10px;border:1px solid var(--line);padding:8px 14px}
.live-chat .dot{width:34px;height:34px;border-radius:50%;background:var(--band)}
.live-chat b{color:var(--red);font-size:16px;display:block;line-height:1.2}
.live-chat span{font-size:11px;color:var(--muted)}
.contact-block{font-size:13px;color:var(--muted);line-height:1.8}
.contact-block b{color:var(--ink)}
.contact-block .ic{display:inline-block;width:16px;height:16px;border-radius:50%;background:var(--blue);vertical-align:-3px;margin-right:6px}
.basket{display:flex;align-items:center;gap:8px;font-size:13px;color:var(--muted);margin-top:6px}
.basket .box{border:1px solid var(--line);padding:3px 10px;color:var(--ink);font-weight:600}

/* nav */
.main-nav{height:40px;background:var(--white);border-top:1px solid var(--line);border-bottom:1px solid var(--line)}
.main-nav ul{list-style:none;display:flex;width:1120px;margin:0 auto;height:38px;align-items:center}
.main-nav li{font-size:14px;padding:0 16px;height:38px;line-height:38px;color:var(--ink);border-right:1px solid var(--line)}
.main-nav li.active{color:var(--blue);font-weight:600;border-bottom:3px solid var(--blue)}

/* hero */
.hero{position:relative;height:520px;background:linear-gradient(135deg,#c9b79c 0%,#a8916f 45%,#7d6a52 100%);overflow:hidden}
.hero-photo{position:absolute;inset:0}
.hero-caption{position:absolute;left:230px;top:210px;width:560px;height:120px;background:rgba(40,40,40,.55);padding:14px 22px;color:var(--white)}
.hero-caption h2{font-size:40px;font-weight:700;font-style:normal;line-height:1.1}
.hero-caption p{font-size:18px;font-style:italic;opacity:.9}
.price-badge{position:absolute;left:600px;top:100px;width:140px;height:140px;border-radius:50%;background:var(--white);text-align:center;padding-top:30px;box-shadow:0 4px 12px rgba(0,0,0,.2)}
.price-badge span{font-size:15px;color:var(--muted);display:block}
.price-badge b{font-size:48px;color:var(--red);font-family:"Raleway",sans-serif;line-height:1}
.offer-badge{position:absolute;left:810px;top:180px;width:240px;height:240px;border-radius:50%;background:var(--red);color:var(--white);text-align:center;padding-top:56px}
.offer-badge h3{font-size:44px;font-weight:700;line-height:1.05}
.offer-badge p{font-size:18px;margin-top:10px}
.hero-dots{position:absolute;bottom:26px;left:0;right:0;display:flex;justify-content:center;gap:10px}
.hero-dots i{width:12px;height:12px;border-radius:50%;background:rgba(255,255,255,.6)}
.hero-dots i.on{background:var(--white)}

/* intro */
.intro{padding-top:34px;text-align:center}
.intro h1{font-size:26px;font-weight:700;color:var(--ink)}
.services{display:flex;gap:30px;margin-top:30px;text-align:left}
.service{flex:1}
.service h4{font-size:14px;color:var(--blue);font-weight:700;margin-bottom:4px}
.service p{font-size:12px;color:var(--muted);line-height:1.6}
.help-btn{display:inline-block;margin-top:56px;background:var(--blue);color:var(--white);font-size:22px;font-weight:600;padding:12px 44px;border-radius:4px}

/* categories */
.categories{margin-top:38px;height:320px;background:var(--band);padding-top:40px}
.categories .wrap{display:flex;gap:40px}
.category{flex:1;position:relative;height:240px}
.category .thumb{height:240px}
.category .label{position:absolute;left:0;right:0;bottom:0;height:56px;background:rgba(0,0,0,.55);color:var(--white);font-family:"Raleway",sans-serif;font-size:22px;font-weight:600;text-align:center;line-height:56px}

/* featured */
.featured{height:480px;background:var(--white);text-align:center;padding-top:40px}
.section-tag{display:inline-block;border:1px solid var(--line);padding:8px 36px;font-family:"Raleway",sans-serif;font-size:22px;font-weight:700;background:var(--white)}
.products{display:flex;gap:36px;margin-top:34px;text-align:left}
.product{flex:1}
.product .thumb{height:240px;border:1px solid var(--line)}
.product h4{font-size:14px;font-weight:700;margin-top:12px}
.product .row{display:flex;justify-content:space-between;align-items:center;margin-top:8px}
.product .from{font-size:12px;color:var(--muted);line-height:1.3}
.product .from b{color:var(--blue);font-size:14px;display:block}
.btn-shop{background:var(--blue);color:var(--white);font-weight:700;font-size:14px;padding:8px 20px;border-radius:3px}

/* about + offers */
.about-offers{border-top:1px solid var(--line);padding-top:40px;height:500px}
.about-offers .wrap{display:flex;gap:60px}
.about{flex:0 0 640px}
.about h2{font-size:24px;font-weight:700;margin-bottom:18px}
.about p{font-size:13px;color:var(--muted);margin-bottom:16px;line-height:1.75}
.btn-outline{display:inline-block;border:2px solid var(--blue);color:var(--blue);font-weight:600;padding:8px 26px;border-radius:3px;margin-top:10px}
.offers{flex:1}
.offers h3{font-size:24px;font-weight:700;border-bottom:2px solid var(--blue);padding-bottom:8px;margin-bottom:18px}
.offer{display:flex;gap:16px;align-items:center;border:1px solid var(--line);padding:12px;margin-bottom:16px}
.offer .thumb{width:70px;height:70px;background:linear-gradient(135deg,#dfeef6,#9ccbe3)}
.offer .text{flex:1;font-size:12px;color:var(--muted)}
.offer .text b{display:block;color:var(--ink);font-size:14px}
.offer .price{text-align:center;color:var(--red);font-family:"Raleway",sans-serif;font-weight:700;font-size:34px;line-height:1}
.offer .price small{display:block;font-size:12px}

/* blog */
.recent-blog{height:180px}
.recent-blog h2{font-size:26px;font-weight:700;margin-bottom:18px}
.posts{display:flex;gap:40px}
.post{flex:1;display:flex;gap:18px}
.post .thumb{width:110px;height:90px}
.post h4{font-size:14px;color:var(--blue);font-weight:700}
.post .date{font-size:11px;color:var(--muted)}
.post p{font-size:12px;color:var(--muted);margin-top:4px}

/* footer */
.site-footer{background:var(--footer);color:#ccc;height:248px;padding-top:34px}
.footer-cols{display:flex;gap:40px}
.footer-col{flex:1;font-size:12px;line-height:2}
.footer-col h4{color:var(--white);font-size:18px;font-weight:700;margin-bottom:8px}
.social{display:flex;gap:10px;margin-top:8px}
.social i{width:30px;height:30px;border-radius:50%;background:#444}
.payments{display:flex;gap:8px;margin-top:18px}
.payments i{width:44px;height:26px;background:#555;border-radius:3px}
.footer-base{background:var(--footer-base);height:48px;color:#999;font-size:11px;text-align:center;line-height:48px}
</style>
</head>
<body>

<header class="site-header">
  <div class="wrap">
    <div class="brand"><span class="brand-square"></span><span class="brand-name">Quillbrook.com</span></div>
    <div class="header-right">
      <div class="live-chat"><span class="dot"></span><div><b>Live chat</b><span>Chat with our team</span></div></div>
      <div>
        <div class="contact-block">
          <div><span class="ic"></span>CALL · FREE: <b>01632 960 418</b></div>
          <div><span class="ic"></span>EMAIL: <b>hello@quillbrook.com</b></div>
        </div>
        <div class="basket">Your basket: <span class="box">£0.00</span></div>
      </div>
    </div>
  </div>
</header>

<nav class="main-nav">
  <ul>
    <li class="active">Home</li><li>About</li><li>Printing</li><li>Graphic design</li><li>Website design</li><li>Artwork guide</li><li>Sample pack</li><li>Upload</li><li>Testimonials</li><li>Blog</li><li>Contact us</li>
  </ul>
</nav>

<section class="hero">
  <div class="hero-photo" role="img" aria-label="Desk scene with printed leaflets, flyers and stationery seen from above"></div>
  <div class="price-badge"><span>Starting from</span><b>44£</b></div>
  <div class="hero-caption">
    <h2>Leaflets &amp; Flyers</h2>
    <p>Sed ut ac lorem rutrum, quis nunc in nulla sed velit dolore eu fugiat</p>
  </div>
  <div class="offer-badge"><h3>Special<br>offers</h3><p>50% onwards</p></div>
  <div class="hero-dots"><i></i><i></i><i class="on"></i><i></i><i></i></div>
</section>

<section class="intro">
  <div class="wrap">
    <h1>Flyer Printing, Leaflet Printing, Brochure Printing</h1>
    <div class="services">
      <div class="service"><h4>Flyer Printing</h4><p>We print flyer printing and leaflet printing products at low prices. We offer a wide range of leaflet printing and flyer printing products at different sizes and paper.</p></div>
      <div class="service"><h4>Brochure Printing</h4><p>We print flyer printing and leaflet printing products at low prices. We offer a wide range of leaflet printing and flyer printing products at different sizes and paper.</p></div>
      <div class="service"><h4>Digital Printing</h4><p>We print flyer printing and leaflet printing products at low prices. We offer a wide range of leaflet printing and flyer printing products at different sizes and paper.</p></div>
      <div class="service"><h4>Giant Printing</h4><p>We print flyer printing and leaflet printing products at low prices. We offer a wide range of leaflet printing and flyer printing products at different sizes and paper.</p></div>
    </div>
    <span class="help-btn">Need help or advice?</span>
  </div>
</section>

<section class="categories">
  <div class="wrap">
    <div class="category"><div class="thumb" role="img" aria-label="Stack of printed business cards" style="background:linear-gradient(135deg,#e8eef2,#9fb3c0)"></div><div class="label">Popular Products</div></div>
    <div class="category"><div class="thumb" role="img" aria-label="Colourful party flyer collection" style="background:linear-gradient(135deg,#3a3a3a,#8a8a8a)"></div><div class="label">Excellent Collection</div></div>
    <div class="category"><div class="thumb" role="img" aria-label="Grid of print design templates" style="background:linear-gradient(135deg,#5a7a9a,#c2a15a)"></div><div class="label">Browse Templates</div></div>
  </div>
</section>

<section class="featured">
  <div class="wrap">
    <span class="section-tag">Featured Products</span>
    <div class="products">
      <div class="product"><div class="thumb" role="img" aria-label="Business cards mock-up" style="background:linear-gradient(135deg,#3d3d3d,#9a9a9a)"></div><h4>Business Cards</h4><div class="row"><span class="from">Start From<b>£10.00</b></span><span class="btn-shop">SHOP NOW</span></div></div>
      <div class="product"><div class="thumb" role="img" aria-label="Folded leaflet mock-up" style="background:linear-gradient(135deg,#e6f1e4,#6fb36a)"></div><h4>Folded Leaflets &amp; Flyers</h4><div class="row"><span class="from">Start From<b>£10.00</b></span><span class="btn-shop">SHOP NOW</span></div></div>
      <div class="product"><div class="thumb" role="img" aria-label="Leaflets and flyers mock-up" style="background:linear-gradient(135deg,#e3f2f8,#33a6d7)"></div><h4>Leaflets &amp; Flyers</h4><div class="row"><span class="from">Start From<b>£10.00</b></span><span class="btn-shop">SHOP NOW</span></div></div>
      <div class="product"><div class="thumb" role="img" aria-label="Letterhead stationery mock-up" style="background:linear-gradient(135deg,#f2f2f2,#a9a9a9)"></div><h4>A4 Letterheads</h4><div class="row"><span class="from">Start From<b>£10.00</b></span><span class="btn-shop">SHOP NOW</span></div></div>
    </div>
  </div>
</section>

<section class="about-offers">
  <div class="wrap">
    <div class="about">
      <h2>Proin gravida nibh vel velit auctor aliquet</h2>
      <p>We print flyer printing and leaflet printing products at low prices. We offer a wide range of leaflet printing and flyer printing products at different sizes and paper weights. Our leaflet printing prices include free delivery within the UK. Our standard turnaround is 2-7 working days however if you require your flyer printing job quicker we can even offer 24 hour print as standard in most cases.</p>
      <p>We offer gloss flyers and silk flyers and can apply different finishes should you require. Send us your own artwork or use our design team and we are confident that you will come back time and time again.</p>
      <span class="btn-outline">Learn more about us</span>
    </div>
    <div class="offers">
      <h3>Special Offers</h3>
      <div class="offer"><div class="thumb" role="img" aria-label="Brochure sample"></div><div class="text"><b>Brochure Printing</b>Lorem ipsum dolor sit amet consectetur</div><div class="price">40<small>£££</small></div></div>
      <div class="offer"><div class="thumb" role="img" aria-label="Brochure sample"></div><div class="text"><b>Brochure Printing</b>Lorem ipsum dolor sit amet consectetur</div><div class="price">40<small>£££</small></div></div>
    </div>
  </div>
</section>

<section class="recent-blog">
  <div class="wrap">
    <h2>Recent Blog</h2>
    <div class="posts">
      <div class="post"><div class="thumb" role="img" aria-label="Flyer printing samples" style="background:linear-gradient(135deg,#f4d36a,#33a6d7)"></div><div><h4>Leaflet printing and flyer printing</h4><span class="date">14 Aug 2024</span><p>We print flyer printing products at low prices. We offer a wide range of leaflet printing and flyer printing products.</p></div></div>
      <div class="post"><div class="thumb" role="img" aria-label="Printed stationery on a desk" style="background:linear-gradient(135deg,#6b5a48,#c9b79c)"></div><div><h4>Get your quality print printing from us</h4><span class="date">14 Aug 2024</span><p>We print flyer printing products at low prices. We offer a wide range of leaflet printing and flyer printing products.</p></div></div>
    </div>
  </div>
</section>

<footer class="site-footer">
  <div class="wrap">
    <div class="footer-cols">
      <div class="footer-col"><h4>GET In Touch</h4>Mon to Fri 09:00 – 17:30<br>Phone: 01632 960 418<br>Email: hello@quillbrook.com
        <div class="social"><i></i><i></i><i></i></div></div>
      <div class="footer-col"><h4>My Account</h4>Account Login<br>Edit My Details<br>Password Reminder<br>Refer a Friend</div>
      <div class="footer-col"><h4>How to Play</h4>Guide &amp; Video<br>FAQ<br>Game Credit<br>Terms of Play</div>
      <div class="footer-col"><h4>About Us</h4>Behind the Scenes<br>Locations<br>Charity Donations<br>Investor Relations</div>
    </div>
    <div class="payments"><i></i><i></i><i></i><i></i><i></i><i></i></div>
  </div>
</footer>
<div class="footer-base">Registered in England and Wales. Company registration number 00000000. VAT registration</div>

</body>
</html>
```